Packaging & Label Design for CDB Products

We are a European CBD company specialising in athletic recovery, sleep improvement and wellness.

We would like the packaging to incorporate our logo and name (and font 'Codec') 'Meridell CBD'. The design must be transferable to all of our products. CBD Oils, Balms, Lip Balm and Vape E-Liquid.

We would like it to be simple but eye-catching and modern. We don't want bright colours. Preferred pallet of muted greys, blacks, white and pastel colours. Geometric concepts, possibly using different colours for each item of the range, we are open to new and fresh ideas (we are seeking you for your experience) and when we find the right design we would likely throw more work in your direction..

Our product range is not complete so the designer must be flexible with some changes and provide files where format can be easily edited by packaging manufacturer. We are also waiting for dimensions for the labels and boxes for several products and will supply the designer with full dimensions of all products once selected.

Oil Box: 2.6 x 9.0 x 2.6 cm (open format 16.7 x 11.6cm)
Labels: 7.8 x 3.3 cm (Front and Back)

Our expected product range will be:
CBD Oil 1000mg
CBD Oil 3000mg
CBD Balm 100mg
CBD Balm 300mg
E-Liquid 500mg
Lip Balm 50mg

We look forward to seeing your ideas.

Best Regards
Meridell CBD

```html
<!DOCTYPE html>
<html lang="en">
<head>
<meta charset="utf-8">
<title>Meridell CBD – Oil Drops Packaging</title>
<link href="https://fonts.googleapis.com/css2?family=Montserrat:wght@500;600;700&display=swap" rel="stylesheet">
<style>
  :root {
    --canvas: #ffffff;
    --charcoal: #4a4542;
    --white: #ffffff;
    --blush: #e0a1a6;
    --sage-teal: #72adb3;
    --font-main: "Montserrat", sans-serif;
  }
  * { box-sizing: border-box; margin: 0; padding: 0; }
  html, body {
    width: 1200px; height: 908px; overflow: hidden;
    background: var(--canvas);
    font-family: var(--font-main);
    color: var(--white);
  }
  .canvas { position: relative; width: 1200px; height: 908px; }

  /* Box front panel */
  .box-front {
    position: absolute; top: 101px; width: 273px; height: 739px;
    background: var(--charcoal);
  }
  .box-front .tier-band {
    position: absolute; left: 0; right: 0; top: 482px; bottom: 0;
  }
  .box-front .frame {
    position: absolute; left: 16px; right: 16px; top: 15px; bottom: 16px;
    border: 2px solid var(--white);
  }
  .box-front .divider {
    position: absolute; left: 16px; right: 16px; height: 2px; background: var(--white);
  }
  .box-front .divider--top { top: 497px; }
  .box-front .divider--bottom { top: 665px; }

  .brand-mark {
    position: absolute; left: 0; right: 0; text-align: center;
  }
  .brand-mark .dot {
    display: block; margin: 0 auto;
    border: 2px solid var(--white); border-radius: 50%;
  }
  .brand-mark .name {
    display: block; font-weight: 700; text-transform: uppercase; white-space: nowrap;
  }

  .box-front .brand-mark { top: 150px; }
  .box-front .brand-mark .dot { width: 42px; height: 42px; margin-bottom: 22px; }
  .box-front .brand-mark .name { font-size: 19px; letter-spacing: 2.5px; }

  .product-title { position: absolute; left: 0; right: 0; text-align: center; font-weight: 700; }
  .product-title .cbd { display: block; line-height: 1; }
  .product-title .drops { display: block; line-height: 1; }

  .box-front .product-title { top: 338px; }
  .box-front .product-title .cbd { font-size: 52px; letter-spacing: 2px; }
  .box-front .product-title .drops { font-size: 25px; margin-top: 2px; letter-spacing: 1px; }

  .variant { position: absolute; left: 0; right: 0; text-align: center; font-weight: 500; }
  .box-front .variant { top: 504px; font-size: 20px; letter-spacing: 9px; padding-left: 9px; }

  .strength { position: absolute; left: 0; right: 0; text-align: center; font-weight: 600; }
  .box-front .strength { top: 681px; font-size: 23px; }

  /* Bottle label */
  .bottle-label {
    position: absolute; top: 546px; width: 212px; height: 272px;
    background: var(--charcoal);
  }
  .bottle-label .tier-band {
    position: absolute; left: 0; right: 0; top: 191px; bottom: 0;
  }
  .bottle-label .frame {
    position: absolute; left: 8px; right: 8px; top: 8px; bottom: 9px;
    border: 2px solid var(--white);
  }
  .bottle-label .divider {
    position: absolute; left: 8px; right: 8px; top: 200px; height: 2px; background: var(--white);
  }
  .bottle-label .brand-mark { top: 28px; }
  .bottle-label .brand-mark .dot { width: 30px; height: 30px; margin-bottom: 16px; }
  .bottle-label .brand-mark .name { font-size: 13px; letter-spacing: 1.6px; }
  .bottle-label .product-title { top: 134px; }
  .bottle-label .product-title .cbd { font-size: 31px; letter-spacing: 1px; }
  .bottle-label .product-title .drops { font-size: 16px; }
  .bottle-label .variant { top: 204px; font-size: 18px; letter-spacing: 2px; }
  .bottle-label .strength { top: 236px; font-size: 20px; }

  .tier--1000 .tier-band { background: var(--blush); }
  .tier--3000 .tier-band { background: var(--sage-teal); }
</style>
</head>
<body>
<main class="canvas">

  <section class="box-front tier--1000" style="left:68px;">
    <div class="tier-band"></div>
    <div class="frame"></div>
    <div class="divider divider--top"></div>
    <div class="divider divider--bottom"></div>
    <div class="brand-mark"><span class="dot"></span><span class="name">Meridell CBD</span></div>
    <h2 class="product-title"><span class="cbd">CBD</span><span class="drops">oil drops</span></h2>
    <p class="variant">natural</p>
    <p class="strength">1000 mg</p>
  </section>

  <section class="bottle-label tier--1000" style="left:383px;">
    <div class="tier-band"></div>
    <div class="frame"></div>
    <div class="divider"></div>
    <div class="brand-mark"><span class="dot"></span><span class="name">Meridell CBD</span></div>
    <h2 class="product-title"><span class="cbd">CBD</span><span class="drops">oil drops</span></h2>
    <p class="variant">natural</p>
    <p class="strength">1000 mg</p>
  </section>

  <section class="box-front tier--3000" style="left:654px;">
    <div class="tier-band"></div>
    <div class="frame"></div>
    <div class="divider divider--top"></div>
    <div class="divider divider--bottom"></div>
    <div class="brand-mark"><span class="dot"></span><span class="name">Meridell CBD</span></div>
    <h2 class="product-title"><span class="cbd">CBD</span><span class="drops">oil drops</span></h2>
    <p class="variant">natural</p>
    <p class="strength">3000 mg</p>
  </section>

  <section class="bottle-label tier--3000" style="left:968px;">
    <div class="tier-band"></div>
    <div class="frame"></div>
    <div class="divider"></div>
    <div class="brand-mark"><span class="dot"></span><span class="name">Meridell CBD</span></div>
    <h2 class="product-title"><span class="cbd">CBD</span><span class="drops">oil drops</span></h2>
    <p class="variant">natural</p>
    <p class="strength">3000 mg</p>
  </section>

</main>
</body>
</html>
```